Property Developer - Simple yet Sophisticated and Sharp Business Card

We are a medium sized property developer involved mainly in townhouse developments and land subdivisions.

The company is looking for a simple, sharp and sophisticated business card that will be given to contractors, land owners, financiers etc and thus will need to look professional.

Property development related graphics and art can be used, however the card is not to be too "busy" or crowded. Our company name is KL Estates which could possibly be incorporated into the graphics or artwork.

Single sided and/or double sided designs will be acceptable.

A Simple, Sophisticated, Sharp design please!

Good Luck !

```html
<!DOCTYPE html>
<html lang="en">
<head>
<meta charset="utf-8">
<title>KL Estates – Business Card</title>
<link rel="stylesheet" href="https://fonts.googleapis.com/css2?family=Bebas+Neue&display=swap">
<style>
  :root {
    --canvas: #ffffff;
    --card: #58585a;
    --card-edge: #3d4682;
    --text-grey: #a7a9ac;
    --text-white: #ffffff;
    --brand-green: #8dc63f;
  }
  html, body {
    margin: 0;
    padding: 0;
    width: 1200px;
    height: 900px;
    overflow: hidden;
    background: var(--canvas);
  }
  .sheet {
    display: block;
    width: 1200px;
    height: 900px;
  }
  .sheet text {
    font-family: "Bebas Neue", "Oswald", sans-serif;
  }
  .card-face { fill: var(--card); stroke: var(--card-edge); stroke-width: 1.2; }
  .contact-line { fill: var(--text-grey); }
  .holder-name { fill: var(--text-white); }
  .company-name { fill: var(--brand-green); }
</style>
</head>
<body>
<svg class="sheet" viewBox="0 0 1200 900" xmlns="http://www.w3.org/2000/svg" role="img" aria-label="KL Estates business card, portrait and landscape versions">
  <defs>
    <g id="landscape-card">
      <rect class="card-face" x="0" y="0" width="405" height="248"/>
      <text class="company-name" font-size="36" textLength="236" lengthAdjust="spacingAndGlyphs" transform="translate(5,4) rotate(90)">KL ESTATES</text>
      <text class="contact-line" x="40" y="50" font-size="50" textLength="352" lengthAdjust="spacingAndGlyphs">PHONE: (07) 3555 0182</text>
      <text class="contact-line" x="40" y="94" font-size="50" textLength="300" lengthAdjust="spacingAndGlyphs">FAX: (07) 3555 0196</text>
      <text class="holder-name" x="43" y="184" font-size="96" textLength="350" lengthAdjust="spacingAndGlyphs">YOUR NAME</text>
      <text class="contact-line" x="40" y="210" font-size="22" textLength="353" lengthAdjust="spacingAndGlyphs">EMAIL: PROJECTS.KLESTATES@MAILBOX.COM</text>
      <text class="contact-line" x="40" y="238" font-size="27" textLength="353" lengthAdjust="spacingAndGlyphs">PO BOX 2468, HILLCREST NORTH QLD 4118</text>
    </g>
  </defs>

  <!-- Portrait card -->
  <g class="portrait-card">
    <rect class="card-face" x="57" y="66" width="465" height="760"/>
    <text class="contact-line" font-size="100" textLength="655" lengthAdjust="spacingAndGlyphs" transform="translate(155,750) rotate(-90)">PHONE: (07) 3555 0182</text>
    <text class="contact-line" font-size="105" textLength="560" lengthAdjust="spacingAndGlyphs" transform="translate(240,750) rotate(-90)">FAX: (07) 3555 0196</text>
    <text class="holder-name" font-size="200" textLength="662" lengthAdjust="spacingAndGlyphs" transform="translate(405,748) rotate(-90)">YOUR NAME</text>
    <text class="contact-line" font-size="43" textLength="662" lengthAdjust="spacingAndGlyphs" transform="translate(455,750) rotate(-90)">EMAIL: PROJECTS.KLESTATES@MAILBOX.COM</text>
    <text class="contact-line" font-size="57" textLength="662" lengthAdjust="spacingAndGlyphs" transform="translate(505,750) rotate(-90)">PO BOX 2468, HILLCREST NORTH QLD 4118</text>
    <text class="company-name" x="65" y="818" font-size="76" textLength="450" lengthAdjust="spacingAndGlyphs">KL ESTATES</text>
  </g>

  <!-- Fanned stack of landscape cards -->
  <g class="card-stack">
    <use href="#landscape-card" x="606" y="311"/>
    <use href="#landscape-card" x="655" y="352"/>
    <use href="#landscape-card" x="703" y="390"/>
    <use href="#landscape-card" x="750" y="428"/>
  </g>
</svg>
</body>
</html>
```